The Little Meadow Biscuit Bakery Swing Tag Label Design/Logo

Hi! We are looking for a “swing tag” label design for our different flavoured packs of (6) cookies. Basic info on the front (business name “The Little Meadow Biscuit Bakery”, strap line being “Handmade Gourmet Cookies” (not made in Norfolk) and the flavour “Choc Chip”, “Original”, “Choc Orange”, etc…).
The flavour part of the label being colour coded to suit, so dark brown for choc chip, beige for original, orange for choc orange, red/white for cranberry & white choc, bla bla bla!!
The rear of the tag to display ingredients, barcode, business postcode, suitable for Vegans, Dairy Free, Fenwick Approved Logo and Net Weight 300g.
Packaging is clear cellophane bags, with crimp seal. Three cookies stacked side by side with a brown Jute string tied around the packaging which will hold the tag.
We are selling in farm shops, deli’s and local food stores, so want to have a modern/smart feel to the design, yet retain the appeal of a small “cottage industry/countryside” style business.
The attached image is where we have got so far (with our very basic design skills) , but do not let this guide you too much, as we are looking for inspiration. (Appreciate the attached does not have the cottage/country appeal)!!
Size is undetermined, but thinking 100mm x 50mm, ish? Not ruled out a round label either, being cookies?
Labels will also be the basis for our business cards, internet pages (facebook, Instagram, etc…), so the design wants to be catchy, instantly recognisable and “say what it does on the tin”.
We also have single pack cookies in cellophane bags, so would be great if the deign could be printed in sticky label format also.
Not decided if the labels will be “craft paper” brown tags, or white, or another colour. Open to suggestions.
Like the idea of the “bite” out of the cookie, but needs “some teeth” if you get what I mean.
Feel free to message if you wish!
Thanks for your time.

Logo Text

The Little Meadow Biscuit Bakery or THE LITTLE MEADOW BISCUIT BAKERY

```html
<!DOCTYPE html>
<html lang="en">
<head>
<meta charset="utf-8">
<title>The Little Meadow Biscuit Bakery – Flavour Labels</title>
<link href="https://fonts.googleapis.com/css2?family=Quicksand:wght@500;600&display=swap" rel="stylesheet">
<style>
  :root {
    --page: #ffffff;
    --cranberry: #b5121b;
    --cranberry-soft: #d98f86;
    --cranberry-fill: #a8201f;
    --orange: #f0a020;
    --orange-soft: #f5d09c;
    --orange-fill: #f9ac3e;
    --original: #d8b88e;
    --original-text: #a06e2c;
    --original-soft: #e6caa3;
    --original-fill: #e2cca4;
    --chip: #c28e5a;
    --chip-text: #a5682c;
    --chip-soft: #d8b48c;
    --chip-fill: #b17a45;
  }
  html, body {
    margin: 0;
    width: 1200px;
    height: 1200px;
    overflow: hidden;
    background: var(--page);
  }
  .label-sheet {
    position: relative;
    width: 1200px;
    height: 1200px;
    font-family: "Quicksand", sans-serif;
  }
  .label {
    position: absolute;
    width: 310px;
    height: 310px;
  }
  .label--cranberry { left: 270px; top: 275px; }
  .label--orange    { left: 600px; top: 275px; }
  .label--original  { left: 270px; top: 595px; }
  .label--chip      { left: 600px; top: 595px; }
  .brand-name { font-size: 20.5px; font-weight: 500; }
  .strapline  { font-size: 19px; font-weight: 500; letter-spacing: 0.3px; }
  .flavour    { font-size: 21px; font-weight: 600; letter-spacing: 1.5px; }
  .flavour--small { font-size: 13px; letter-spacing: 0.6px; }
</style>
</head>
<body>
<main class="label-sheet">
  <svg width="0" height="0" style="position:absolute" aria-hidden="true">
    <defs>
      <path id="arc-brand" d="M -104.3,38 A 111 111 0 1 1 104.3,38"/>
      <path id="arc-strap" d="M -117.8,31.6 A 122 122 0 0 0 117.8,31.6"/>
      <path id="arc-flavour" d="M -74,42 A 85 85 0 0 0 74,42"/>
    </defs>
  </svg>

  <svg class="label label--cranberry" viewBox="-155 -155 310 310">
    <circle r="139" fill="var(--cranberry)"/>
    <circle r="139" fill="none" stroke="var(--cranberry)" stroke-width="20" stroke-linecap="round" stroke-dasharray="0 31.19"/>
    <circle r="135" fill="#fff"/>
    <circle r="129" fill="none" stroke="var(--cranberry-soft)" stroke-width="3"/>
    <path d="M -62,-20 C -58,-62 -10,-78 28,-62 C 66,-46 72,0 56,26 C 38,52 -10,60 -42,44 C -66,30 -64,8 -62,-20 Z" fill="var(--cranberry-fill)" role="img" aria-label="Illustrated cranberry and white chocolate cookie with a bite taken out"/>
    <text class="brand-name" fill="var(--cranberry)"><textPath href="#arc-brand" startOffset="50%" text-anchor="middle">The Little Meadow Biscuit Bakery</textPath></text>
    <text class="flavour flavour--small" fill="var(--cranberry)"><textPath href="#arc-flavour" startOffset="50%" text-anchor="middle">CRANBERRY &amp; WHITE CHOC</textPath></text>
    <text class="strapline" fill="var(--cranberry-soft)"><textPath href="#arc-strap" startOffset="50%" text-anchor="middle">Handmade Gourmet Cookies</textPath></text>
  </svg>

  <svg class="label label--orange" viewBox="-155 -155 310 310">
    <circle r="139" fill="var(--orange)"/>
    <circle r="139" fill="none" stroke="var(--orange)" stroke-width="20" stroke-linecap="round" stroke-dasharray="0 31.19"/>
    <circle r="135" fill="#fff"/>
    <circle r="129" fill="none" stroke="var(--orange-soft)" stroke-width="3"/>
    <path d="M -62,-20 C -58,-62 -10,-78 28,-62 C 66,-46 72,0 56,26 C 38,52 -10,60 -42,44 C -66,30 -64,8 -62,-20 Z" fill="var(--orange-fill)" role="img" aria-label="Illustrated chocolate orange cookie with a bite taken out"/>
    <text class="brand-name" fill="var(--orange)"><textPath href="#arc-brand" startOffset="50%" text-anchor="middle">The Little Meadow Biscuit Bakery</textPath></text>
    <text class="flavour" fill="var(--orange)"><textPath href="#arc-flavour" startOffset="50%" text-anchor="middle">CHOC ORANGE</textPath></text>
    <text class="strapline" fill="var(--orange-soft)"><textPath href="#arc-strap" startOffset="50%" text-anchor="middle">Handmade Gourmet Cookies</textPath></text>
  </svg>

  <svg class="label label--original" viewBox="-155 -155 310 310">
    <circle r="139" fill="var(--original)"/>
    <circle r="139" fill="none" stroke="var(--original)" stroke-width="20" stroke-linecap="round" stroke-dasharray="0 31.19"/>
    <circle r="135" fill="#fff"/>
    <circle r="129" fill="none" stroke="var(--original-soft)" stroke-width="3"/>
    <path d="M -62,-20 C -58,-62 -10,-78 28,-62 C 66,-46 72,0 56,26 C 38,52 -10,60 -42,44 C -66,30 -64,8 -62,-20 Z" fill="var(--original-fill)" role="img" aria-label="Illustrated original butter cookie with a bite taken out"/>
    <text class="brand-name" fill="var(--original-text)"><textPath href="#arc-brand" startOffset="50%" text-anchor="middle">The Little Meadow Biscuit Bakery</textPath></text>
    <text class="flavour" fill="var(--original-text)"><textPath href="#arc-flavour" startOffset="50%" text-anchor="middle">ORIGINAL</textPath></text>
    <text class="strapline" fill="var(--original-soft)"><textPath href="#arc-strap" startOffset="50%" text-anchor="middle">Handmade Gourmet Cookies</textPath></text>
  </svg>

  <svg class="label label--chip" viewBox="-155 -155 310 310">
    <circle r="139" fill="var(--chip)"/>
    <circle r="139" fill="none" stroke="var(--chip)" stroke-width="20" stroke-linecap="round" stroke-dasharray="0 31.19"/>
    <circle r="135" fill="#fff"/>
    <circle r="129" fill="none" stroke="var(--chip-soft)" stroke-width="3"/>
    <path d="M -62,-20 C -58,-62 -10,-78 28,-62 C 66,-46 72,0 56,26 C 38,52 -10,60 -42,44 C -66,30 -64,8 -62,-20 Z" fill="var(--chip-fill)" role="img" aria-label="Illustrated chocolate chip cookie with a bite taken out"/>
    <text class="brand-name" fill="var(--chip-text)"><textPath href="#arc-brand" startOffset="50%" text-anchor="middle">The Little Meadow Biscuit Bakery</textPath></text>
    <text class="flavour" fill="var(--chip-text)"><textPath href="#arc-flavour" startOffset="50%" text-anchor="middle">CHOC CHIP</textPath></text>
    <text class="strapline" fill="var(--chip-text)"><textPath href="#arc-strap" startOffset="50%" text-anchor="middle">Handmade Gourmet Cookies</textPath></text>
  </svg>
</main>
</body>
</html>
```